Wordpress Design for a Digital Management Consulting Business

I need a simple Wordpress Design and someone to set it up for a new boutique management consulting business called Tallowby Advisory that specialises in providing strategic advice to help grow digital businesses. It covers business strategy, marketing strategy, digital strategy, web product development, marketing campaigns, social, search, etc. From strategy to implementation.

URL is: tallowbyadvisory.com.au

My professional background is here: au.examplenet.com/in/maresquillon

Competitors: other boutique digital/marketing management consulting businesses in Australia

The logos, colours and fonts are attached.

I would like the site to convey a business that is Smart/intelligent, Contemporary, Progressive, Digital, Energetic, Friendly.

The objective of the site is to educate visitors about what Tallowby Advisory does and encourage them to contact me for more information. It will be very light on content.

Target Market(s)

CEOs/Managing Directors, General Managers, Marketing Directors

Industry/Entity Type

Management Consulting

Font styles to use
Sans Serif

Colors
e34197
5c5c5c
000000

Requirements
Must have
• Site design requirements:
• Choose an appropriate Wordpress template, set it up for me and let me be able to edit it ongoing.
• It should use lots of images - these can be inspirational and not necessarily tied directly to the work
• Pink should feature, but not be the dominant colour.
• Site structure should be:
• 1. Home page - image led with horizontal navigation. Text beneath and images to describe the services.
• 2. About page - with space to write text and insert a picture of the Director
• 3. Services - with space to highlight services either as a list or graphically with text
• 4. Contact page - with space to write text and add email links, etc.
• Should have horizontal navigation
• It should have the flexibility to add another page
Nice to have
• Use the tree icon somehow in the design - consider in the background enlarged
• Use pink, grey, black from logo. Can introduce another complimentary colour if necessary.
• Can introduce another complimentary font to go with the logo font.
Should not have
• Use cliched business images and icons, eg. business suits, hand shakes, business men, business ties.

```html
<!DOCTYPE html>
<html lang="en">
<head>
<meta charset="utf-8">
<title>Tallowby Advisory — Professional Consulting Services</title>
<link rel="stylesheet" href="https://fonts.googleapis.com/css2?family=Montserrat:wght@400;600;700&family=Open+Sans:wght@400;600;700&display=swap">
<style>
:root{
  --pink:#e34197;
  --grey:#5c5c5c;
  --black:#000000;
  --ink:#2b2b2b;
  --light:#f1f1f1;
  --line:#d6d6d6;
  --footer:#262626;
  --footer-deep:#1a1a1a;
  --white:#ffffff;
}
*{margin:0;padding:0;box-sizing:border-box}
html,body{width:1200px;height:2400px;overflow:hidden}
body{font-family:"Open Sans",Arial,sans-serif;color:var(--grey);background:var(--white)}
h1,h2,h3,.nav a,.btn,.brand{font-family:"Montserrat",Arial,sans-serif}

/* Hero */
.hero{position:relative;height:720px;overflow:hidden}
.hero-photo{position:absolute;inset:0;background:linear-gradient(135deg,#6d7480 0%,#3d434c 45%,#22262c 100%)}
.hero-shade{position:absolute;inset:0;background:linear-gradient(180deg,rgba(0,0,0,.15),rgba(0,0,0,.45))}
.site-header{position:absolute;top:0;left:0;right:0;height:120px;display:flex;align-items:center;justify-content:space-between;padding:0 0 0 60px}
.brand{display:flex;align-items:center;gap:14px;background:var(--white);padding:20px 26px;color:var(--pink);font-size:26px;font-weight:700;letter-spacing:1px}
.brand-mark{width:22px;height:22px;background:var(--pink)}
.nav{display:flex;height:76px;background:var(--pink);padding-left:16px}
.nav a{display:flex;align-items:center;padding:0 24px;color:var(--white);font-size:15px;font-weight:600;text-decoration:none;letter-spacing:.5px}
.nav a.active{background:var(--footer)}
.hero-copy{position:absolute;top:250px;left:0;right:0;text-align:center;color:var(--white)}
.hero-copy h1{font-size:92px;font-weight:700;letter-spacing:6px;line-height:1}
.hero-copy .sub{font-family:"Montserrat",sans-serif;font-size:34px;font-weight:600;letter-spacing:5px;margin-top:22px}
.hero-copy .tag{font-size:24px;letter-spacing:2px;margin-top:34px}
.btn{display:inline-block;margin-top:48px;padding:16px 30px;border:2px solid var(--white);color:var(--white);font-size:18px;letter-spacing:1px;text-decoration:none}

/* Welcome */
.welcome{height:280px;text-align:center;padding-top:42px}
.welcome-mark{width:26px;height:26px;background:var(--pink);margin:0 auto 16px}
.welcome h2{font-size:34px;font-weight:600;color:var(--ink);letter-spacing:1px}
.welcome p{width:980px;margin:22px auto 0;font-size:16px;line-height:1.6}

/* Section heading */
.section-title{display:flex;align-items:center;justify-content:center;gap:24px;font-size:32px;font-weight:600;color:var(--ink);letter-spacing:2px}
.section-title::before,.section-title::after{content:"";width:360px;height:2px;background:var(--line)}

/* Services */
.services{height:520px;background:var(--light);padding-top:44px}
.cards{display:flex;gap:48px;justify-content:center;align-items:stretch;margin-top:36px}
.card{width:320px;display:flex;flex-direction:column}
.card-photo{height:160px;flex:none}
.p1{background:linear-gradient(135deg,#2d3a4a,#6c7b8c)}
.p2{background:linear-gradient(135deg,#c9d3dc,#8fa2b3)}
.p3{background:linear-gradient(135deg,#1e4f82,#7fa9d4)}
.card h3{font-size:24px;font-weight:600;color:var(--ink);margin-top:14px}
.card p{font-size:14px;line-height:1.5;margin-top:8px;min-height:105px}
.card .more{display:block;font-family:"Montserrat",sans-serif;font-size:13px;font-weight:700;color:var(--ink);margin-top:10px}

/* What we do */
.what{height:580px;padding-top:40px}
.pillars{display:flex;justify-content:center;gap:120px;margin-top:40px}
.pillar{width:280px;text-align:center}
.pillar svg{display:block;margin:0 auto}
.pillar h3{font-size:24px;font-weight:600;color:var(--ink);margin-top:20px}
.pillar p{font-size:14px;line-height:1.5;margin-top:10px}

/* Footer */
.site-footer{height:240px;background:var(--footer);color:#cfcfcf;display:flex;padding:28px 80px 0;gap:60px}
.site-footer h4{font-family:"Montserrat",sans-serif;color:var(--white);font-size:20px;font-weight:600;margin-bottom:14px}
.site-footer ul{list-style:none;font-size:13px;line-height:1.75}
.site-footer li::before{content:"";display:inline-block;width:6px;height:6px;background:var(--white);border-radius:50%;margin-right:10px;vertical-align:middle}
.foot-nav{width:170px}
.foot-services{width:520px}
.foot-services .cols{display:flex;gap:60px}
.foot-contact{width:320px;font-size:13px;line-height:1.6}
.foot-contact strong{color:var(--white)}
.socials{display:flex;gap:10px;margin-top:12px}
.socials span{width:18px;height:18px;border-radius:50%;background:#9a9a9a}
.legal{height:40px;background:var(--footer-deep);color:#bbbbbb;font-size:12px;display:flex;align-items:center;justify-content:center}
</style>
</head>
<body>

<section class="hero">
  <div class="hero-photo" role="img" aria-label="Photograph of a desk with business papers, charts and a laptop"></div>
  <div class="hero-shade"></div>
  <header class="site-header">
    <div class="brand"><span class="brand-mark"></span>Tallowby Advisory</div>
    <nav class="nav">
      <a class="active" href="#">HOME</a>
      <a href="#">ABOUT US</a>
      <a href="#">SERVICES</a>
      <a href="#">PROJECTS</a>
      <a href="#">NEWS</a>
      <a href="#">CONTACT US</a>
    </nav>
  </header>
  <div class="hero-copy">
    <h1>PROFESSIONAL</h1>
    <div class="sub">CONSULTING SERVICES</div>
    <div class="tag">WE ARE THE TRUSTED ADVISOR TO THE WORLD'S LEADING BUSINESSES</div>
    <a class="btn" href="#">LEARN MORE</a>
  </div>
</section>

<section class="welcome">
  <div class="welcome-mark"></div>
  <h2>WELCOME TO TALLOWBY ADVISORY</h2>
  <p>Tallowby Advisory is a boutique management consulting company advising businesses in the digital, ecommerce, media, travel, technology and finance sectors on business, product and marketing strategy. Combining strategic thinking with digital knowhow and marketing expertise, Tallowby Advisory works with businesses looking to accelerate growth, diversify or increase profit of a new or existing digital business.</p>
</section>

<section class="services">
  <h2 class="section-title">OUR SERVICES</h2>
  <div class="cards">
    <article class="card">
      <div class="card-photo p1" role="img" aria-label="Photograph of a person working on a tablet with digital graphics"></div>
      <h3>Digital Strategy</h3>
      <p>With over 15 years experience in digital businesses, Tallowby Advisory develops business, product, sales and marketing strategies with a focus on accelerating or establishing digital businesses.</p>
      <a class="more" href="#">READ MORE</a>
    </article>
    <article class="card">
      <div class="card-photo p2" role="img" aria-label="Illustration of marketing charts and sketches on a whiteboard"></div>
      <h3>Marketing Consultation</h3>
      <p>Whether you have a new product or want to accelerate growth of an existing business, Tallowby Advisory can deliver a robust marketing strategy and implement a successful campaign.</p>
      <a class="more" href="#">READ MORE</a>
    </article>
    <article class="card">
      <div class="card-photo p3" role="img" aria-label="Photograph of a hand touching a glowing digital network screen"></div>
      <h3>Digital Transformation</h3>
      <p>Tallowby Advisory works with businesses to create a digital competitive advantage, identifying new opportunities and building digital capabilities.</p>
      <a class="more" href="#">READ MORE</a>
    </article>
  </div>
</section>

<section class="what">
  <h2 class="section-title">WHAT WE DO</h2>
  <div class="pillars">
    <div class="pillar">
      <svg width="200" height="200" viewBox="0 0 200 200" aria-hidden="true">
        <polygon points="100,8 180,54 180,146 100,192 20,146 20,54" fill="var(--pink)"/>
        <circle cx="100" cy="100" r="36" fill="none" stroke="#fff" stroke-width="6"/>
        <circle cx="100" cy="100" r="18" fill="none" stroke="#fff" stroke-width="6"/>
        <circle cx="100" cy="100" r="5" fill="#fff"/>
      </svg>
      <h3>Strategic thinking</h3>
      <p>Working with CEO, MDs and Functional leaders, Tallowby Advisory evaluates business problems and identifies new opportunities for growth.</p>
    </div>
    <div class="pillar">
      <svg width="200" height="200" viewBox="0 0 200 200" aria-hidden="true">
        <polygon points="100,8 180,54 180,146 100,192 20,146 20,54" fill="#fff" stroke="var(--line)" stroke-width="3"/>
        <polyline points="62,124 88,96 108,112 138,76" fill="none" stroke="var(--grey)" stroke-width="7" stroke-linecap="round" stroke-linejoin="round"/>
        <polyline points="120,76 138,76 138,94" fill="none" stroke="var(--grey)" stroke-width="7" stroke-linecap="round" stroke-linejoin="round"/>
      </svg>
      <h3>Analytical approach</h3>
      <p>Recommendations are based on consultation with key stakeholders, in-depth analysis, industry, competitor and customer insight, and testing.</p>
    </div>
    <div class="pillar">
      <svg width="200" height="200" viewBox="0 0 200 200" aria-hidden="true">
        <polygon points="100,8 180,54 180,146 100,192 20,146 20,54" fill="#fff" stroke="var(--line)" stroke-width="3"/>
        <circle cx="100" cy="100" r="26" fill="none" stroke="var(--grey)" stroke-width="14" stroke-dasharray="10 6"/>
        <circle cx="100" cy="100" r="10" fill="none" stroke="var(--grey)" stroke-width="5"/>
      </svg>
      <h3>Implementation</h3>
      <p>Tallowby Advisory will develop a road map to implement the strategy, embed the changes within your organisation or run an end-to-end project.</p>
    </div>
  </div>
</section>

<footer>
  <div class="site-footer">
    <div class="foot-nav">
      <h4>Navigation</h4>
      <ul><li>Home</li><li>About Us</li><li>Services</li><li>Projects</li><li>News</li><li>Contact Us</li></ul>
    </div>
    <div class="foot-services">
      <h4>Our Services</h4>
      <div class="cols">
        <ul><li>Digital Strategy</li><li>Business Strategy</li><li>Product and Content Strategy</li><li>Growth Strategy</li><li>Sales and Marketing Strategy</li></ul>
        <ul><li>Digital Strategy</li><li>Business Strategy</li><li>Product and Content Strategy</li><li>Growth Strategy</li><li>Sales and Marketing Strategy</li></ul>
      </div>
    </div>
    <div class="foot-contact">
      <h4>Get in Touch</h4>
      <p><strong>For more information about what we do, please contact:</strong><br>
      Mares Quillon (Director)<br>Tallowby Advisory<br>m: 0400 218 653<br>e: mares@tallowbyadvisory.com.au</p>
      <div class="socials"><span></span><span></span><span></span><span></span><span></span></div>
    </div>
  </div>
  <div class="legal">Tallowby Advisory © 2015 &nbsp;Privacy policy</div>
</footer>

</body>
</html>
```